Digital Medical Care Start-up: New Web Design Needed

We are a startup in Boston, USA. Our current website has mostly acceptable content but looks outdated and it is ineffective. Viewers - especially possible investors - are turned off. It may also have too much content - especially the table. Current site Https://CareLoomKits.com

Business: we produce apps for surgeons to give their patients. The apps describe the medical procedure they will have, how to prepare, what to do to speed recovery, and how to interpret any symptoms. One app for each medical procedure - there are over 200.

LIKES
https://www.kestrivamed.com/
https://www.fenworthclinix.com/en/
https://zorandi.com/about/
DISLIKES
https://plax-ora.com/
https://www.tundravita.com/
https://www.grelvin-clinic.net/
https://www.quessa.com/

Target Market(s)

Audience: Medical Surgeons (customers) and Investors (we will do our first capital raise afterward the new website) in USA.

Coding

Number of Pages Required

Font styles to use
Other font styles liked:
• Candara

Colors
0455a3
f37122

Requirements
Must have
• OUTPUT:
We want a fully Responsive Version.
We do not use Wordpress. The page layout (or template) should be html + css + images + a little JavaScript.
The first page is the landing page. The second page would be the template on which we put the remaining content.
After delivery, the html would be merged into the existing framework. The site needs to be built on a template so it can be managed by an average quasi-tech person, without the need for a coder.

See exisiting company and product logos. They will remain unchanged, so make sure the website is compatable with the current logos.
Nice to have
• We have attached an idea of ours. This is meant for your stimulation, not necessarily for replication. Our attachment does not have all the content details, but the outline is correct.

```html
<!DOCTYPE html>
<html lang="en">
<head>
<meta charset="utf-8">
<title>CareLoomKits – Procedure eCare</title>
<link href="https://fonts.googleapis.com/css2?family=Cabin:wght@400;500;600;700&family=Arimo:ital,wght@0,400;0,700;1,400;1,700&display=swap" rel="stylesheet">
<style>
:root{
  --blue:#0455a3;
  --blue-mid:#1a6fc4;
  --orange:#f37122;
  --ink:#1b1b1b;
  --text:#555;
  --light:#f4f4f4;
  --black:#000;
  --white:#fff;
}
*{box-sizing:border-box;margin:0;padding:0}
html,body{width:1200px;height:4405px;overflow:hidden}
body{position:relative;font-family:"Arimo",Arial,sans-serif;color:var(--ink);background:var(--white)}
.abs{position:absolute}
.head-font{font-family:"Cabin",sans-serif}

/* top bar */
.topbar{top:0;left:0;width:1200px;height:60px}
.brand{left:99px;top:8px;display:flex;align-items:center;gap:10px}
.brand-mark{width:42px;height:42px;border-radius:50%;background:var(--blue)}
.brand-name{font-family:"Cabin",sans-serif;font-weight:700;font-size:26px;color:var(--blue)}
.hours{right:465px;top:10px;text-align:right;font-size:10px;color:#444;line-height:1.25}
.hours b{font-size:11px;color:var(--ink)}
.top-phone{left:760px;top:17px;display:flex;align-items:center;gap:10px;font-weight:700;font-size:17px}
.btn{display:flex;align-items:center;justify-content:center;gap:8px;border-radius:22px;font-weight:700;text-transform:uppercase}
.top-email{left:930px;top:11px;width:169px;height:38px;background:var(--orange);color:var(--white);font-size:12px}

/* nav */
.nav{top:60px;left:0;width:1200px;height:44px;background:var(--blue)}
.nav ul{list-style:none;display:flex;justify-content:space-between;align-items:center;width:1002px;margin-left:99px;height:44px;color:var(--white);font-size:14px;font-weight:700}

/* hero */
.hero{top:104px;left:0;width:1200px;height:583px;background:linear-gradient(100deg,#f3f3f1 0%,#e8e6e2 40%,#d9cfc6 70%,#c8a98a 100%)}
.hero-kicker{left:99px;top:180px;font-family:"Cabin",sans-serif;font-size:36px;color:#222;letter-spacing:.5px}
.hero-title{left:97px;top:215px;font-family:"Cabin",sans-serif;font-weight:700;font-size:66px;color:#222}
.hero-title span{color:var(--blue)}
.hero-sub{left:99px;top:298px;font-family:"Cabin",sans-serif;font-size:22px;color:#333}
.hero-cta{left:101px;top:345px;width:168px;height:46px;background:var(--orange);color:var(--white);font-size:14px}
.hero-arrow{top:270px;width:20px;height:36px}
.dots{left:565px;top:548px;display:flex;gap:8px}
.dots i{width:10px;height:10px;border:1.5px solid #fff;border-radius:50%}
.dots i.on{background:#fff}

/* services */
.services-title{top:770px;left:0;width:1200px;text-align:center;font-family:"Cabin",sans-serif;font-weight:600;font-size:33px;line-height:40px}
.cards{top:877px;left:99px;width:1002px;display:flex;gap:23px}
.card{width:318px;height:330px;background:var(--white);box-shadow:0 0 10px rgba(0,0,0,.12);text-align:center;padding-top:34px}
.icon-circle{width:92px;height:92px;border-radius:50%;background:var(--blue);margin:0 auto;display:flex;align-items:center;justify-content:center}
.card h3{font-family:"Cabin",sans-serif;font-weight:500;font-size:22px;margin:16px 0 10px}
.card p{font-size:11.5px;line-height:23px;color:var(--text);padding:0 15px}
.more{color:var(--orange);font-weight:700;font-size:13px;margin-top:6px}

/* schedule band */
.band{left:0;width:1200px;height:111px;background:var(--orange);color:var(--white)}
.band h2{position:absolute;left:99px;top:32px;font-family:"Cabin",sans-serif;font-weight:500;font-size:33px}
.band .phone{position:absolute;left:640px;top:42px;display:flex;align-items:center;gap:6px;font-size:20px;font-weight:700}
.band .email{position:absolute;left:830px;top:29px;width:269px;height:54px;background:var(--white);color:var(--orange);font-size:17px;border-radius:28px}

/* split */
.split{top:1412px;left:0;width:1200px;height:735px;background:var(--light)}
.team-photo{left:0;top:0;width:600px;height:735px;background:linear-gradient(160deg,#c9c1b5 0%,#b0a48f 35%,#2b4f8f 70%,#1e3a78 100%)}
.split h2{position:absolute;left:642px;top:86px;font-family:"Cabin",sans-serif;font-weight:600;font-size:31px;line-height:40px}
.features{position:absolute;left:642px;top:180px;list-style:none;width:460px}
.features li{height:93px}
.features h4{display:flex;align-items:center;gap:8px;font-size:19px;font-weight:700}
.radio{width:15px;height:15px;border:2px solid var(--blue);border-radius:50%;display:flex;align-items:center;justify-content:center}
.radio::after{content:"";width:7px;height:7px;border-radius:50%;background:var(--blue)}
.features p{font-size:11.5px;line-height:22px;color:var(--text);padding-left:25px;margin-top:4px}

/* testimonials */
.testimonials{top:2147px;left:0;width:1200px;height:496px;background:linear-gradient(180deg,#1466bd,#0a5cb4)}
.testimonials h2{position:absolute;width:100%;top:82px;text-align:center;color:var(--white);font-family:"Cabin",sans-serif;font-weight:600;font-size:40px}
.quote{top:155px;width:474px;height:172px;background:var(--white);border-radius:6px;padding:24px 20px;font-size:12.5px;line-height:26px;color:#333}
.quote::after{content:"";position:absolute;right:110px;bottom:-30px;border-left:44px solid transparent;border-top:30px solid var(--white)}
.author{top:342px;display:flex;align-items:center;gap:12px;color:var(--white)}
.avatar{width:60px;height:60px;border-radius:50%;background:linear-gradient(135deg,#e8e2da,#9c8c7c);border:3px solid #dfe7f2}
.author b{font-style:italic;font-size:18px;display:block}
.author span{font-size:13.5px}
.t-arrow{top:225px;width:16px;height:32px}
.lorem-tag{left:180px;top:476px;font-size:13px;color:#111}

/* clinical groups */
.groups-title{top:2838px;left:0;width:1200px;text-align:center;font-family:"Cabin",sans-serif;font-weight:600;font-size:43px}
.grid{top:2911px;left:99px;width:1002px;display:grid;grid-template-columns:repeat(3,318px);column-gap:23px;row-gap:26px}
.group{height:393px;background:var(--white);box-shadow:0 0 10px rgba(0,0,0,.1);text-align:center}
.group .ph{height:235px}
.group h3{font-size:22px;font-weight:700;margin:26px 0 10px;color:#222}
.group h5{font-size:13px;font-weight:700;margin-bottom:10px}
.group p{font-size:11.5px;line-height:21px;color:var(--text);padding:0 18px}

/* cta */
.cta{top:3820px;left:0;width:1200px;height:236px;background:var(--orange);color:var(--white);text-align:center}
.cta h2{position:absolute;width:100%;top:62px;font-family:"Cabin",sans-serif;font-weight:500;font-size:31px}
.cta .c-phone{position:absolute;left:323px;top:122px;width:270px;height:54px;border:1.5px solid var(--white);font-size:20px}
.cta .c-email{position:absolute;left:607px;top:122px;width:270px;height:54px;background:var(--white);color:var(--orange);font-size:17px}

/* footer */
.footer{top:4056px;left:0;width:1200px;height:349px;background:var(--black);color:var(--white)}
.f-brand{left:99px;top:70px;display:flex;align-items:center;gap:16px}
.f-brand .brand-mark{width:66px;height:66px;background:var(--white)}
.f-brand .brand-name{color:var(--white);font-size:38px;font-weight:600}
.socials{left:182px;top:156px;display:flex;gap:16px}
.socials i{width:46px;height:46px;border:1.5px solid var(--white);border-radius:50%}
.f-col h4{font-size:15px;font-weight:700;margin-bottom:10px}
.f-col li{list-style:none;font-size:13px;line-height:26px}
.sitemap{left:574px;top:68px}
.contact{left:857px;top:68px}
.contact li{display:flex;gap:14px;align-items:flex-start;line-height:19px;margin-bottom:14px}
.contact svg{flex:none;margin-top:2px}
.copy{left:0;top:315px;width:1200px;text-align:center;font-size:11.5px}
</style>
</head>
<body>

<header class="abs topbar">
  <div class="abs brand"><div class="brand-mark"></div><span class="brand-name">CARELOOMKITS</span></div>
  <div class="abs hours"><b>Operator Avaiable</b><br>Monday to Saturday<br>8 am to 9 pm</div>
  <div class="abs top-phone">
    <svg width="22" height="22" viewBox="0 0 24 24" fill="none" stroke="#f37122" stroke-width="2"><path d="M5 3h4l2 5-3 2a11 11 0 0 0 6 6l2-3 5 2v4a2 2 0 0 1-2 2A17 17 0 0 1 3 5a2 2 0 0 1 2-2z"/></svg>
    617-555-0142
  </div>
  <div class="abs btn top-email">Email us today</div>
</header>

<nav class="abs nav">
  <ul><li>HOME</li><li>I</li><li>ABOUT US</li><li>I</li><li>MEDICAL ADVISORY BOARD</li><li>I</li><li>CLINICAL GROUPS</li><li>I</li><li>TESTIMONIALS</li><li>I</li><li>CONTACT</li></ul>
</nav>

<section class="abs hero" role="img" aria-label="Photo of a patient holding a tablet on a video call with a doctor">
  <div class="abs hero-kicker">DIGITALLY DELIVERING</div>
  <h1 class="abs hero-title">Procedure <span>eCare</span></h1>
  <div class="abs hero-sub">For 100+ procedures Quicky and economically</div>
  <div class="abs btn hero-cta">Contact us</div>
  <svg class="abs hero-arrow" style="left:60px" viewBox="0 0 20 36" fill="none" stroke="#333" stroke-width="2"><path d="M16 2L3 18l13 16"/></svg>
  <svg class="abs hero-arrow" style="left:1114px" viewBox="0 0 20 36" fill="none" stroke="#333" stroke-width="2"><path d="M4 2l13 16L4 34"/></svg>
  <div class="abs dots"><i></i><i></i><i></i><i class="on"></i></div>
</section>

<h2 class="abs services-title">We Enable Clinicians To Increase The Number<br>Of Procedures -While Improving Health Outcomes</h2>
<div class="abs cards">
  <article class="card">
    <div class="icon-circle"><svg width="44" height="50" viewBox="0 0 44 50" fill="none" stroke="#fff" stroke-width="2.5"><rect x="4" y="6" width="36" height="42" rx="3"/><rect x="14" y="2" width="16" height="8" rx="2"/><path d="M10 20l3 3 5-5M22 21h12M10 31l3 3 5-5M22 32h12M10 42h24"/></svg></div>
    <h3>Periop Tasks</h3>
    <p>Lorem ipsum dolor sit amet, cocttur adipiscing elit, sed do eiusmod tempor incidunt ut laboret dolore magna aliqua. is ipssuspendisse ultrices gravida. Risus commodo</p>
    <div class="more">LEARN MORE &nbsp;»</div>
  </article>
  <article class="card">
    <div class="icon-circle"><svg width="48" height="48" viewBox="0 0 48 48" fill="none" stroke="#fff" stroke-width="2.5"><rect x="10" y="4" width="30" height="30" rx="2"/><path d="M25 10v12M19 16h12"/><circle cx="14" cy="32" r="5"/><path d="M4 46c0-6 4-9 10-9s10 3 10 9"/></svg></div>
    <h3>Interactive Symptom Triage</h3>
    <p>Lorem ipsum dolor sit amet, cocttur adipiscing elit, sed do eiusmod tempor incidunt ut laboret dolore magna aliqua. is ipssuspendisse ultrices gravida. Risus commodo</p>
    <div class="more">LEARN MORE &nbsp;»</div>
  </article>
  <article class="card">
    <div class="icon-circle"><svg width="50" height="48" viewBox="0 0 50 48" fill="none" stroke="#fff" stroke-width="2.5"><rect x="6" y="4" width="38" height="16" rx="3"/><path d="M12 10h26M12 15h18"/><circle cx="14" cy="30" r="5"/><circle cx="36" cy="30" r="5"/><path d="M4 46c0-6 4-9 10-9s10 3 10 9M26 46c0-6 4-9 10-9s10 3 10 9"/></svg></div>
    <h3>Communications</h3>
    <p>Lorem ipsum dolor sit amet, cocttur adipiscing elit, sed do eiusmod tempor incidunt ut laboret dolore magna aliqua. is ipssuspendisse ultrices gravida. Risus commodo</p>
    <div class="more">LEARN MORE &nbsp;»</div>
  </article>
</div>

<section class="abs band" style="top:1301px">
  <h2>Schedule an Appointment Today</h2>
  <div class="phone"><svg width="20" height="20" viewBox="0 0 24 24" fill="none" stroke="#fff" stroke-width="2"><path d="M5 3h4l2 5-3 2a11 11 0 0 0 6 6l2-3 5 2v4a2 2 0 0 1-2 2A17 17 0 0 1 3 5a2 2 0 0 1 2-2z"/></svg>617-555-0142</div>
  <div class="btn email"><svg width="24" height="18" viewBox="0 0 24 18" fill="none" stroke="#f37122" stroke-width="2"><rect x="1" y="1" width="22" height="16" rx="1"/><path d="M1 1l11 9 11-9"/></svg>Email us today</div>
</section>

<section class="abs split">
  <div class="abs team-photo" role="img" aria-label="Photo of a team of smiling doctors and nurses in scrubs"></div>
  <h2>We Have The Best Ecare Soultion<br>For Surgeries And Treatments</h2>
  <ul class="features">
    <li><h4><span class="radio"></span>Improvements In The Entire Patient Journey</h4><p>Lorem ipsum dolor sit amet, consectetur adipiscing elit, sed do eiuod tempor incididunt ut labore et dolore magna aliqua. Lorem ipsum</p></li>
    <li><h4><span class="radio"></span>Immediate And Measurable Benefits</h4><p>Lorem ipsum dolor sit amet, consectetur adipiscing elit, sed do eiuod tempor incididunt ut labore et dolore magna aliqua. Lorem ipsum</p></li>
    <li><h4><span class="radio"></span>Provider Specific</h4><p>Lorem ipsum dolor sit amet, consectetur adipiscing elit, sed do eiuod tempor incididunt ut labore et dolore magna aliqua. Lorem ipsum</p></li>
    <li><h4><span class="radio"></span>Accessible From Any Device</h4><p>Lorem ipsum dolor sit amet, consectetur adipiscing elit, sed do eiuod tempor incididunt ut labore et dolore magna aliqua. Lorem ipsum</p></li>
    <li><h4><span class="radio"></span>No User Manual Needed</h4><p>Lorem ipsum dolor sit amet, consectetur adipiscing elit, sed do eiuod tempor incididunt ut labore et dolore magna aliqua. Lorem ipsum</p></li>
  </ul>
</section>

<section class="abs testimonials">
  <h2>Testimonials</h2>
  <svg class="abs t-arrow" style="left:74px" viewBox="0 0 16 32" fill="none" stroke="#fff" stroke-width="2"><path d="M14 2L2 16l12 14"/></svg>
  <svg class="abs t-arrow" style="left:1104px" viewBox="0 0 16 32" fill="none" stroke="#fff" stroke-width="2"><path d="M2 2l12 14L2 30"/></svg>
  <blockquote class="abs quote" style="left:118px">The CareLoomKits Peri-op eCare app provides patients with critical information about their diagnosis and treatment. This service guides patients through what is often a very stressful experience, answering common questions that arise during the course of treatment. It's a fantastic support tool for both doctors and patients."</blockquote>
  <blockquote class="abs quote" style="left:608px">The CareLoomKits Peri-op eCare app provides patients with critical information about their diagnosis and treatment. This service guides patients through what is often a very stressful experience, answering common questions that arise during the course of treatment. It's a fantastic support tool for both doctors and patients."</blockquote>
  <div class="abs author" style="left:122px"><div class="avatar" role="img" aria-label="Portrait of the reviewer"></div><div><b>Jerome T. Halvers, MD</b><span>Associate Professor, Orthopaedic Surgery</span></div></div>
  <div class="abs author" style="left:612px"><div class="avatar" role="img" aria-label="Portrait of the reviewer"></div><div><b>Jerome T. Halvers, MD</b><span>Associate Professor, Orthopaedic Surgery</span></div></div>
  <div class="abs lorem-tag">Lorem Ipsum</div>
</section>

<section class="abs band" style="top:2643px">
  <h2>Schedule an Appointment Today</h2>
  <div class="phone"><svg width="20" height="20" viewBox="0 0 24 24" fill="none" stroke="#fff" stroke-width="2"><path d="M5 3h4l2 5-3 2a11 11 0 0 0 6 6l2-3 5 2v4a2 2 0 0 1-2 2A17 17 0 0 1 3 5a2 2 0 0 1 2-2z"/></svg>617-555-0142</div>
  <div class="btn email"><svg width="24" height="18" viewBox="0 0 24 18" fill="none" stroke="#f37122" stroke-width="2"><rect x="1" y="1" width="22" height="16" rx="1"/><path d="M1 1l11 9 11-9"/></svg>Email us today</div>
</section>

<h2 class="abs groups-title">Clinical Groups</h2>
<div class="abs grid">
  <article class="group"><div class="ph" role="img" aria-label="Medical illustration of a stomach" style="background:radial-gradient(circle at 55% 50%,#b9726a,#9b2a1e 55%,#6f1710)"></div><h3>BARIATRIC</h3><h5>Dorian B. Lenske, MD MS FASMBS</h5><p>Professor of Surgery, Brookfield<br>Medical School.</p></article>
  <article class="group"><div class="ph" role="img" aria-label="Illustration of a glowing heart inside a chest" style="background:radial-gradient(circle at 50% 55%,#c0392b,#1b4f9c 35%,#071a3d 80%)"></div><h3>CARDIAC SURGERY</h3><h5>Joel Smedrik, MD MS FASMBS</h5><p>Sed ut perspiciatis unde omnis iste<br>natus error sit voluptatem</p></article>
  <article class="group"><div class="ph" role="img" aria-label="Photo of a microscope in a fertility laboratory" style="background:linear-gradient(135deg,#e8eef5,#b8c8dc 50%,#7d98bd)"></div><h3>FERTILITY MEDICINE</h3><h5>Arlen K. Stovik Md</h5><p>Associate Professor of Obstetrics,<br>Gynecology and Reproductive Biology<br>Brookfield Medical School</p></article>
  <article class="group"><div class="ph" role="img" aria-label="Illustration of a uterus held in a doctor's hands" style="background:radial-gradient(circle at 50% 55%,#e9a9b4,#f0dde0 50%,#e9e9ea)"></div><h3>GYNECOLOGY</h3><h5>Corwin S. Atterly, MD MBA</h5><p>Assistant Professor of Obstetrics, Gynecology and Reproductive Biology, Brookfield Medical School. Vice President, Brookfield Medical Faculty Physicians.</p></article>
  <article class="group"><div class="ph" role="img" aria-label="Photo of a knee surgery in progress" style="background:linear-gradient(135deg,#9fc2de,#e9c8b5 50%,#c9d8e6)"></div><h3>THE STANDARD</h3><h5>Joel Smedrik, MD MS FASMBS</h5><p>Sed ut perspiciatis unde omnis iste<br>natus error sit voluptatem</p></article>
  <article class="group"><div class="ph" role="img" aria-label="Photo of surgeons operating in a theatre" style="background:linear-gradient(135deg,#a9c7e3,#3d6fa8 50%,#1e3f6b)"></div><h3>THE STANDARD</h3><h5>Joel Smedrik, MD MS FASMBS</h5><p>Sed ut perspiciatis unde omnis iste<br>natus error sit voluptatem</p></article>
</div>

<section class="abs cta">
  <h2>Ready to see how CareLoomKits can improve your patient care?</h2>
  <div class="btn c-phone" style="border-radius:28px;text-transform:none"><svg width="20" height="20" viewBox="0 0 24 24" fill="none" stroke="#fff" stroke-width="2"><path d="M5 3h4l2 5-3 2a11 11 0 0 0 6 6l2-3 5 2v4a2 2 0 0 1-2 2A17 17 0 0 1 3 5a2 2 0 0 1 2-2z"/></svg>617-555-0142</div>
  <div class="btn c-email" style="border-radius:28px"><svg width="24" height="18" viewBox="0 0 24 18" fill="none" stroke="#f37122" stroke-width="2"><rect x="1" y="1" width="22" height="16" rx="1"/><path d="M1 1l11 9 11-9"/></svg>Email us today</div>
</section>

<footer class="abs footer">
  <div class="abs f-brand"><div class="brand-mark"></div><span class="brand-name">CARELOOMKITS</span></div>
  <div class="abs socials"><i></i><i></i><i></i></div>
  <div class="abs f-col sitemap"><h4>SITE MAP</h4><ul><li>Home</li><li>About Us</li><li>Medical Advisory Board</li><li>Clinical Groups</li><li>Testimonials</li><li>Contact</li></ul></div>
  <div class="abs f-col contact"><h4>CONTACT US</h4><ul>
    <li><svg width="16" height="20" viewBox="0 0 16 20" fill="#fff"><path d="M8 0a7 7 0 0 0-7 7c0 5 7 13 7 13s7-8 7-13a7 7 0 0 0-7-7zm0 10a3 3 0 1 1 0-6 3 3 0 0 1 0 6z"/></svg><span>CareLoomKits Inc Boston,<br>USA</span></li>
    <li><svg width="16" height="16" viewBox="0 0 24 24" fill="#fff"><path d="M5 2h4l2 5-3 2a11 11 0 0 0 6 6l2-3 5 2v4a2 2 0 0 1-2 2A18 18 0 0 1 3 4a2 2 0 0 1 2-2z"/></svg><span>617-555-0142</span></li>
    <li><svg width="16" height="12" viewBox="0 0 16 12" fill="#fff"><path d="M0 0h16v1L8 7 0 1zM0 3l8 6 8-6v9H0z"/></svg><span>contactus@careloomkitsinc.com</span></li>
  </ul></div>
  <div class="abs copy">©2021 CareLoomKits Inc., CareLoomKits™ and CareLoomKits Inc™ are trademarks of CareLoomKits Inc. &nbsp; Privacy Policy &nbsp;| &nbsp;Terms of &nbsp;| &nbsp;UseLogin</div>
</footer>

</body>
</html>
```